Business card for exciting VC company

Should look simple, crisp, and modern.

Industry/Entity Type

Venture Capital

Contact Information for Business Card

Would like to see at least one design that has our blue on the back with the tagline "Transforming Traditional Industry" and white front with contact details.

Font styles to use
Sans Serif

Requirements
Must have
• Logo

Darius Pellworth
dpellworth@brindlegate.vc
Managing Partner
M (628)304-xxxx

```html
<!DOCTYPE html>
<html lang="en">
<head>
<meta charset="utf-8">
<title>Brindlegate Capital – Business Card Front</title>
<link rel="stylesheet" href="https://fonts.googleapis.com/css2?family=Poppins:ital,wght@0,400;0,500;0,600&display=swap">
<style>
  :root {
    --backdrop: #1d1d1f;
    --card: #ffffff;
    --ink: #111111;
    --brand-blue: #4a86d0;
    --rule: #222222;
  }
  * { box-sizing: border-box; margin: 0; padding: 0; }
  html, body {
    width: 1200px;
    height: 900px;
    overflow: hidden;
    background: var(--backdrop);
    font-family: "Poppins", sans-serif;
  }
  .stage {
    width: 1200px;
    height: 900px;
    display: flex;
    align-items: center;
    justify-content: center;
  }
  .card {
    position: relative;
    width: 1050px;
    height: 600px;
    background: var(--card);
    overflow: hidden;
  }
  .wordmark {
    position: absolute;
    top: 120px;
    left: 0;
    right: 0;
    margin-left: 190px;
    text-align: center;
    font-weight: 600;
    font-size: 48px;
    letter-spacing: 6px;
    color: var(--ink);
    text-transform: uppercase;
    line-height: 1.1;
  }
  .divider {
    position: absolute;
    top: 340px;
    left: 150px;
    width: 800px;
    height: 2px;
    background: var(--rule);
  }
  .person {
    position: absolute;
    top: 358px;
    left: 140px;
  }
  .person-name {
    font-weight: 500;
    font-size: 26px;
    color: var(--ink);
    line-height: 1.2;
  }
  .person-title {
    font-weight: 400;
    font-size: 19px;
    color: var(--brand-blue);
    line-height: 1.3;
  }
  .contacts {
    position: absolute;
    top: 362px;
    right: 80px;
    list-style: none;
    text-align: right;
  }
  .contact-item {
    display: flex;
    align-items: center;
    justify-content: flex-end;
    gap: 14px;
    font-size: 20px;
    color: var(--ink);
    line-height: 1.6;
  }
  .contact-icon { width: 20px; height: 22px; flex: none; }
  .band {
    position: absolute;
    left: 0;
    right: 0;
    bottom: 0;
    height: 20px;
    display: flex;
  }
  .band-dark { width: 46%; background: var(--ink); }
  .band-blue { flex: 1; background: var(--brand-blue); }
</style>
</head>
<body>
  <main class="stage">
    <section class="card" aria-label="Business card front">
      <div class="wordmark">Brindlegate Capital</div>

      <div class="divider"></div>

      <div class="person">
        <p class="person-name">Darius Pellworth</p>
        <p class="person-title">Managing Partner</p>
      </div>

      <ul class="contacts">
        <li class="contact-item">
          <span>(628)304-xxxx</span>
          <svg class="contact-icon" viewBox="0 0 20 22" aria-hidden="true">
            <rect x="4" y="1" width="12" height="20" rx="2" fill="none" stroke="#4a86d0" stroke-width="2"/>
            <line x1="8.5" y1="17.5" x2="11.5" y2="17.5" stroke="#4a86d0" stroke-width="1.6"/>
          </svg>
        </li>
        <li class="contact-item">
          <span>dpellworth@brindlegate.vc</span>
          <svg class="contact-icon" viewBox="0 0 20 22" aria-hidden="true">
            <rect x="1" y="5" width="18" height="12" fill="#4a86d0"/>
            <polyline points="1,5 10,12 19,5" fill="none" stroke="#ffffff" stroke-width="1.6"/>
          </svg>
        </li>
      </ul>

      <div class="band">
        <div class="band-dark"></div>
        <div class="band-blue"></div>
      </div>
    </section>
  </main>
</body>
</html>
```